Prepared Meal Delivery Website

Need a new modern design for a prepared meal delivery company that is hosted on Shopify.

Target Market(s)

Young Professionals

Industry/Entity Type

Prepared Meal Delivery Service

Number of Pages Required

5+ page

Requirements
Must have
• Use https://www.vorabelmeals.com/ as an example
Nice to have
• Vibrant page with call to action obvious and repeated
Should not have
• Generic look, grays/white/black

```html
<!DOCTYPE html>
<html lang="en">
<head>
<meta charset="utf-8">
<title>Dash Meals — Prepared Meal Delivery</title>
<link href="https://fonts.googleapis.com/css2?family=Montserrat:wght@400;500;600;700&family=Mulish:wght@400;600;700&family=Merriweather:wght@400&display=swap" rel="stylesheet">
<style>
:root{
  --orange:#f7941d;
  --dark:#2f2a26;
  --ink:#1f1f1f;
  --muted:#555;
  --light:#f5f5f5;
  --white:#fff;
  --red:#d9163f;
  --green:#5faa1f;
  --grey-arc:#cfcfcf;
}
*{margin:0;padding:0;box-sizing:border-box}
html,body{width:1200px;height:3667px;overflow:hidden}
body{font-family:"Mulish",sans-serif;color:var(--ink);background:var(--white);position:relative}
.abs{position:absolute}
.btn{position:absolute;display:flex;align-items:center;justify-content:center;border-radius:20px;font-family:"Montserrat",sans-serif;font-size:10px;font-weight:600;text-transform:uppercase;color:var(--white);background:var(--orange)}
.btn.dark{background:var(--dark)}
.btn.light{background:var(--white);color:var(--ink)}
.ph{position:absolute}
/* header */
.site-header{left:130px;top:0;width:940px;height:80px;background:var(--dark);border-radius:0 0 22px 22px}
.brand{position:absolute;display:flex;align-items:center;gap:10px;font-family:"Montserrat",sans-serif;font-weight:600;font-size:20px;letter-spacing:4px;text-transform:uppercase;white-space:nowrap}
.brand .sq{width:12px;height:12px;background:var(--orange)}
.site-header .brand{left:16px;top:26px;color:var(--white)}
.nav{position:absolute;left:460px;top:50px;display:flex;gap:37px;font-family:"Montserrat",sans-serif;font-size:11px;color:var(--white)}
.hicon{position:absolute;top:10px;width:16px;height:16px}
.round{position:absolute;top:45px;width:26px;height:26px;border-radius:50%;background:#5b5550}
.cart-badge{position:absolute;left:905px;top:6px;width:14px;height:14px;border-radius:50%;background:var(--orange);font-size:8px;color:#fff;text-align:center;line-height:14px}
/* hero */
.hero{left:0;top:0;width:1200px;height:534px;background:var(--light)}
.hero-dot{left:106px;top:215px;width:60px;height:60px;border-radius:50%;background:#f3dede}
.hero-title{left:130px;top:225px;font-family:"Merriweather",serif;font-weight:400;font-size:38px;line-height:51px;color:var(--ink)}
.hero-title em{font-style:normal;color:var(--orange)}
.hero-text{left:130px;top:346px;width:320px;font-size:13px;line-height:18px;color:#333}
.hero-photo{left:480px;top:147px;width:356px;height:356px;border-radius:50%;background:linear-gradient(135deg,#8d7b6f,#b7b8c6 55%,#6b6a70)}
.steps{left:880px;top:176px;width:200px}
.step{position:absolute;left:0;width:200px}
.step .ic{position:absolute;left:0;top:4px;width:40px;height:40px;border-radius:50%;background:var(--white);box-shadow:0 2px 6px rgba(0,0,0,.08);display:flex;align-items:center;justify-content:center}
.step h4{position:absolute;left:47px;top:0;font-family:"Montserrat",sans-serif;font-weight:500;font-size:15px;white-space:nowrap}
.step p{position:absolute;left:47px;top:22px;width:150px;font-size:9px;line-height:13px;color:#666}
.step hr{position:absolute;left:47px;width:150px;border:0;border-top:1px solid #e2e2e2}
/* titles */
.sec-title{position:absolute;left:0;width:1200px;text-align:center;font-family:"Montserrat",sans-serif;font-weight:500;font-size:33px;color:var(--ink)}
/* bag */
.bag-item{position:absolute;top:668px;width:230px;text-align:center}
.bag-item .pic{width:177px;height:177px;border-radius:50%;margin:0 auto}
.bag-item h3{margin-top:18px;font-family:"Montserrat",sans-serif;font-weight:500;font-size:14.5px;line-height:18px}
.bag-item p{margin-top:8px;font-size:10px;line-height:16px;color:#555}
/* band */
.band{left:0;top:1001px;width:1200px;height:505px;background:linear-gradient(180deg,#4b4857,#5e5b66 60%,#4a4653)}
.band-photo{left:620px;top:1001px;width:580px;height:505px;background:linear-gradient(90deg,rgba(94,91,102,0),#7d7a80 30%,#9a9699 70%,#bdb8ae)}
.band-title{left:130px;top:1065px;font-family:"Montserrat",sans-serif;font-weight:500;font-size:33px;line-height:42px;color:var(--white)}
.band-text{left:130px;top:1178px;width:460px;font-size:12.5px;line-height:20px;color:#eee}
.testi{position:absolute;top:1362px;width:173px;height:173px}
.testi-name{position:absolute;top:1545px;width:173px;text-align:center;font-family:"Montserrat",sans-serif;font-size:11.5px;color:#333}
.under-band{left:0;top:1506px;width:1200px;height:419px;background:var(--light)}
/* who */
.who{position:absolute;top:1690px;width:290px;text-align:center}
.who .who-icon{width:80px;height:80px;margin:0 auto;border-radius:12px;background:linear-gradient(135deg,#fde3c2,#f7c58a)}
.who h3{margin-top:14px;font-family:"Montserrat",sans-serif;font-weight:500;font-size:18px}
.who p{margin-top:8px;font-size:10px;line-height:17px;color:#444}
/* diet */
.diet-text{left:195px;top:2035px;width:810px;text-align:center;font-size:12.5px;line-height:19px;color:#444}
.diet-ring{left:405px;top:2103px;width:390px;height:390px;border-radius:50%;border:2px dotted #777}
.diet-food{left:430px;top:2128px;width:340px;height:340px;border-radius:50%;background:radial-gradient(circle,#e8c39a,#9cae6a 45%,#f2efe9 72%,#fff 73%)}
.diet-label{position:absolute;font-family:"Montserrat",sans-serif;font-weight:500;font-size:17px;letter-spacing:.3px}
.diet-line{position:absolute;height:1px;background:#d8d8d8}
.diet-dot{position:absolute;width:7px;height:7px;border-radius:50%;background:var(--orange)}
/* promo */
.promo{left:0;top:2560px;width:1200px;height:286px;background:var(--orange)}
.promo h2{position:absolute;left:0;top:70px;width:1200px;text-align:center;font-family:"Montserrat",sans-serif;font-weight:500;font-size:33px;color:var(--white)}
.promo p{position:absolute;left:175px;top:128px;width:850px;text-align:center;font-size:12.5px;line-height:19px;color:#fff}
/* newsletter */
.news-bg{left:0;top:2846px;width:1200px;height:408px;background:linear-gradient(90deg,#dcdcda,#ececea 40%,#ececea 60%,#dcdad6)}
.news-left{left:0;top:2846px;width:255px;height:408px;background:radial-gradient(circle at 30% 45%,#8a4a2a,#4f7a2e 55%,#d9d7d2 80%)}
.news-right{left:805px;top:2846px;width:395px;height:408px;background:radial-gradient(circle at 50% 50%,#e2a24c,#d9761f 45%,#cfc6b8 75%)}
.news{left:0;top:2846px;width:1200px;height:408px}
.news h2{position:absolute;left:0;top:135px;width:1200px;text-align:center;font-family:"Montserrat",sans-serif;font-weight:500;font-size:33px}
.news h5{position:absolute;left:0;top:176px;width:1200px;text-align:center;font-family:"Montserrat",sans-serif;font-weight:500;font-size:14px}
.news-input{position:absolute;left:440px;top:201px;width:320px;height:40px;border:1.5px solid #333;border-radius:20px;background:#f3f3f3;display:flex;align-items:center;padding-left:18px;gap:10px;font-size:9px;color:#555}
.news-btn{left:440px;top:249px;width:320px;height:39px}
/* footer */
.footer{left:0;top:3254px;width:1200px;height:413px;background:var(--light)}
.footer .brand{left:155px;top:96px;color:var(--ink)}
.f-logo-box{left:133px;top:76px;width:220px;height:62px;border-radius:6px;background:var(--white)}
.social{position:absolute;top:180px;width:30px;height:30px;border-radius:50%;border:1.5px solid #333;display:flex;align-items:center;justify-content:center}
.fcol{position:absolute;top:78px}
.fcol h6{font-family:"Montserrat",sans-serif;font-weight:600;font-size:14px;color:var(--orange);margin-bottom:14px}
.fcol li{list-style:none;font-size:10px;color:#333;height:24px}
.contact{display:flex;align-items:center;gap:8px;font-size:10px;height:36px;white-space:nowrap}
.contact .ci{width:26px;height:26px;border-radius:50%;border:1.5px solid #333;display:flex;align-items:center;justify-content:center}
.f-rule{left:130px;top:293px;width:940px;height:1px;background:#ddd}
.copy{left:0;top:298px;width:1200px;text-align:center;font-size:10px;color:#333}
.copy span{color:var(--orange)}
.card{position:absolute;top:326px;width:30px;height:19px;border-radius:3px}
</style>
</head>
<body>

<!-- HERO -->
<section class="abs hero" aria-label="Hero">
  <div class="abs hero-dot"></div>
  <h1 class="abs hero-title">Fatest <em>Delivery</em> &amp;<br>Easy <em>Pickup</em></h1>
  <p class="abs hero-text">Sed ut perspiciatis unde omnis iste natus error sit voluptatem accusantium</p>
  <a class="btn" style="left:130px;top:404px;width:133px;height:36px">Shop Meal Plans</a>
  <a class="btn dark" style="left:271px;top:404px;width:133px;height:36px">Order Now</a>

  <svg class="abs" style="left:455px;top:122px" width="406" height="406" viewBox="0 0 406 406" aria-hidden="true">
    <path d="M 30 150 A 185 185 0 0 1 95 40" fill="none" stroke="var(--red)" stroke-width="7" stroke-linecap="round"/>
    <path d="M 300 38 A 185 185 0 0 1 385 145" fill="none" stroke="var(--grey-arc)" stroke-width="7" stroke-linecap="round"/>
    <path d="M 390 250 A 185 185 0 0 1 310 360" fill="none" stroke="var(--green)" stroke-width="7" stroke-linecap="round"/>
  </svg>
  <div class="ph hero-photo" role="img" aria-label="Photo of a smiling woman holding a prepared meal container with a fork"></div>

  <div class="abs steps">
    <div class="step" style="top:0">
      <div class="ic"><svg width="20" height="20" viewBox="0 0 20 20"><rect x="4" y="3" width="12" height="14" rx="1" fill="none" stroke="var(--orange)" stroke-width="1.5"/><path d="M7 7h6M7 10h6M7 13h4" stroke="var(--orange)" stroke-width="1.3"/></svg></div>
      <h4>Choose A Plan</h4>
      <p>Choose one of our pre-set plans, or Build Your Own!</p>
      <hr style="top:70px">
    </div>
    <div class="step" style="top:94px">
      <div class="ic"><svg width="20" height="20" viewBox="0 0 20 20"><path d="M3 6h9v8H3zM12 9h3l2 3v2h-5z" fill="none" stroke="var(--orange)" stroke-width="1.5"/><circle cx="6" cy="15" r="1.5" fill="var(--orange)"/><circle cx="14" cy="15" r="1.5" fill="var(--orange)"/></svg></div>
      <h4>Await Delivery</h4>
      <p>We deliver twice weekly, on Sundays and Wednesdays Our delivery window is between 3 pm and 8 pm</p>
      <hr style="top:100px">
    </div>
    <div class="step" style="top:214px">
      <div class="ic"><svg width="20" height="20" viewBox="0 0 20 20"><path d="M3 9h14v7H3z" fill="var(--orange)"/><path d="M4 9c0-4 12-4 12 0" fill="none" stroke="var(--orange)" stroke-width="1.5"/></svg></div>
      <h4>Heat &amp; Eat</h4>
      <p>Place your meal in the microwave for 2-2.5 minutes or reheat to preferred temperature on a pan/skillet</p>
    </div>
  </div>
</section>

<!-- HEADER -->
<header class="abs site-header">
  <div class="brand"><span class="sq"></span>Dash Meals</div>
  <nav class="nav"><span>Meal Plans</span><span>How It Works</span><span>Testimonials</span><span>App</span><span>FAQ</span></nav>
  <svg class="hicon" style="left:822px" viewBox="0 0 16 16"><circle cx="8" cy="5" r="3" fill="none" stroke="#fff" stroke-width="1.2"/><path d="M2 15c0-4 12-4 12 0" fill="none" stroke="#fff" stroke-width="1.2"/></svg>
  <svg class="hicon" style="left:855px" viewBox="0 0 16 16"><path d="M8 14L2 8a3.3 3.3 0 0 1 6-4 3.3 3.3 0 0 1 6 4z" fill="none" stroke="#fff" stroke-width="1.2"/></svg>
  <svg class="hicon" style="left:889px" viewBox="0 0 16 16"><path d="M1 2h3l2 8h8l1-6H5" fill="none" stroke="#fff" stroke-width="1.2"/><circle cx="7" cy="13" r="1.2" fill="#fff"/><circle cx="13" cy="13" r="1.2" fill="#fff"/></svg>
  <div class="cart-badge">0</div>
  <div class="round" style="left:860px"><svg width="26" height="26" viewBox="0 0 26 26"><circle cx="12" cy="12" r="4" fill="none" stroke="#fff" stroke-width="1.3"/><path d="M15 15l3 3" stroke="#fff" stroke-width="1.3"/></svg></div>
  <div class="round" style="left:892px"><svg width="26" height="26" viewBox="0 0 26 26" fill="#fff"><circle cx="9" cy="9" r="1.3"/><circle cx="13" cy="9" r="1.3"/><circle cx="17" cy="9" r="1.3"/><circle cx="9" cy="13" r="1.3"/><circle cx="13" cy="13" r="1.3"/><circle cx="17" cy="13" r="1.3"/><circle cx="9" cy="17" r="1.3"/><circle cx="13" cy="17" r="1.3"/><circle cx="17" cy="17" r="1.3"/></svg></div>
</header>

<!-- BAG -->
<section aria-label="What's in the bag">
  <h2 class="sec-title" style="top:590px">What’s in you Dash Bag?</h2>
  <div class="bag-item" style="left:125px"><div class="pic" role="img" aria-label="Photo of a woman holding a meal delivery tote bag" style="background:linear-gradient(135deg,#b9a58c,#5a4e48)"></div><h3>Delicious Chef-inspired Meals</h3><p>Our meals are designed and prepared by<br>a team of experienced...</p></div>
  <div class="bag-item" style="left:365px"><div class="pic" role="img" aria-label="Photo of a woman unpacking meals outdoors" style="background:linear-gradient(135deg,#7d8f6a,#c9c7b9)"></div><h3>Perfectly Portioned Amounts</h3><p>Each product is comprised of portioned<br>ingredients to guarantee...</p></div>
  <div class="bag-item" style="left:605px"><div class="pic" role="img" aria-label="Photo of a young man holding meal containers and a tote bag" style="background:linear-gradient(135deg,#a8b7c4,#d8cbb0)"></div><h3>Responsibly Sourced,quality Ingredients</h3><p>Our fresh produce, sustainable seafood,<br>exclusive spice blends...</p></div>
  <div class="bag-item" style="left:845px"><div class="pic" role="img" aria-label="Photo of a woman in a kitchen holding a meal container" style="background:linear-gradient(135deg,#6f5c58,#c5bfb8)"></div><h3>Recyclable Ice Packs And Packaging</h3><p>Our meals and other products are<br>delivered fresh in our specially</p></div>
</section>

<!-- BAND -->
<div class="abs under-band"></div>
<section aria-label="App promotion">
  <div class="abs band"></div>
  <div class="ph band-photo" role="img" aria-label="Photo of a smiling man seated in an armchair eating from a meal container, tote bag beside him"></div>
  <h2 class="abs band-title">We Have<br>Suffered Alteration</h2>
  <p class="abs band-text">Sed ut perspiciatis unde omnis iste natus error sit voluptatem accusantium doloremque laudantium, totam rem aperiam, eaque ipsa quae ab illo inventore veritatis et quasi architecto beatae vitae dicta sunt explicabo.</p>
  <a class="btn" style="left:130px;top:1275px;width:134px;height:36px">Get Your Apps</a>

  <div class="testi" style="left:231px;background:linear-gradient(135deg,#c9ccd0,#8b9096)" role="img" aria-label="Customer photo holding a tote bag"></div>
  <div class="testi" style="left:420px;background:linear-gradient(135deg,#b58a63,#6b5a4d)" role="img" aria-label="Customer photo outdoors eating a meal"></div>
  <div class="testi" style="left:608px;background:linear-gradient(135deg,#dfe3e6,#b9b6a9)" role="img" aria-label="Customer photo with a delivery bag"></div>
  <div class="testi" style="left:796px;background:linear-gradient(135deg,#d1c7ba,#8e8f94)" role="img" aria-label="Customer photo eating at a table"></div>
  <div class="testi-name" style="left:231px">Mara Quill</div>
  <div class="testi-name" style="left:420px">Deon Harlow</div>
  <div class="testi-name" style="left:608px">Ruth Ellery</div>
  <div class="testi-name" style="left:796px">Nina Corvel</div>
</section>

<!-- WHO -->
<section aria-label="Who is it for">
  <h2 class="sec-title" style="top:1614px">Who Is Dash For ?</h2>
  <div class="who" style="left:135px">
    <div class="who-icon" role="img" aria-label="Illustration of a professional with a checklist"></div>
    <h3>Professional</h3>
    <p>Dash is the ideal service for the professional<br>on the go. We deliver twice weekly so you can focus on<br>your career and prioritize...</p>
  </div>
  <div class="who" style="left:455px">
    <div class="who-icon" role="img" aria-label="Illustration of a family group"></div>
    <h3>Families</h3>
    <p>Dash is the ideal service for the professional<br>on the go. We deliver twice weekly so you can focus on<br>your career and prioritize...</p>
  </div>
  <div class="who" style="left:775px">
    <div class="who-icon" role="img" aria-label="Illustration of a single person in a frame"></div>
    <h3>Singles</h3>
    <p>Dash is the ideal service for the professional<br>on the go. We deliver twice weekly so you can focus on<br>your career and prioritize...</p>
  </div>
</section>

<!-- DIET -->
<section aria-label="Meal styles">
  <h2 class="sec-title" style="top:1983px">This isn't Diet-Food</h2>
  <p class="abs diet-text">Sed ut perspiciatis unde omnis iste natus error sit voluptatem accusantium doloremque laudantium, totam rem aperiam, eaque ipsa quae ab illo inventore veritatis et quasi architecto...</p>
  <div class="abs diet-ring"></div>
  <div class="ph diet-food" role="img" aria-label="Photo of stacked meal prep containers with vegetables, salmon and grains"></div>

  <span class="diet-label" style="left:183px;top:2156px">CLEAN</span>
  <span class="diet-dot" style="left:245px;top:2164px"></span><span class="diet-line" style="left:252px;top:2167px;width:200px"></span>
  <span class="diet-label" style="left:965px;top:2156px">KETO</span>
  <span class="diet-dot" style="left:951px;top:2164px"></span><span class="diet-line" style="left:750px;top:2167px;width:201px"></span>

  <span class="diet-label" style="left:215px;top:2287px">VEGAN</span>
  <span class="diet-dot" style="left:284px;top:2295px"></span><span class="diet-line" style="left:291px;top:2298px;width:114px"></span>
  <span class="diet-label" style="left:924px;top:2287px">CLASSIC</span>
  <span class="diet-dot" style="left:910px;top:2295px"></span><span class="diet-line" style="left:795px;top:2298px;width:115px"></span>

  <span class="diet-label" style="left:180px;top:2419px">PALEO</span>
  <span class="diet-dot" style="left:242px;top:2427px"></span><span class="diet-line" style="left:249px;top:2430px;width:203px"></span>
  <span class="diet-label" style="left:965px;top:2419px">MEAL PREP</span>
  <span class="diet-dot" style="left:951px;top:2427px"></span><span class="diet-line" style="left:750px;top:2430px;width:201px"></span>
</section>

<!-- PROMO -->
<section class="abs promo" aria-label="Peak nutrition">
  <h2>Peak Nutrition. Peak Performance.</h2>
  <p>Sed ut perspiciatis unde omnis iste natus error sit voluptatem accusantium doloremque laudantium, totam rem aperiam, eaque ipsa quae ab illo inventore veritatis et quasi architecto beatae vitae dicta sunt explicabo.</p>
  <a class="btn light" style="left:463px;top:183px;width:134px;height:36px">Shop Meal Plans</a>
  <a class="btn dark" style="left:605px;top:183px;width:132px;height:36px">Take The Quiz</a>
</section>

<!-- NEWSLETTER -->
<div class="abs news-bg"></div>
<div class="ph news-left" role="img" aria-label="Photo of grilled chicken with greens and a dipping sauce"></div>
<div class="ph news-right" role="img" aria-label="Photo of a chickpea and rice bowl with lime and chili"></div>
<section class="abs news" aria-label="Newsletter">
  <h2>Newsletter</h2>
  <h5>WHAT ARE YOU WAITING FOR?</h5>
  <div class="news-input"><svg width="16" height="12" viewBox="0 0 16 12"><rect x="1" y="1" width="14" height="10" fill="none" stroke="#333" stroke-width="1.2"/><path d="M1 1l7 6 7-6" fill="none" stroke="#333" stroke-width="1.2"/></svg>Enter Your Email</div>
  <a class="btn news-btn">Subscribe</a>
</section>

<!-- FOOTER -->
<footer class="abs footer">
  <div class="abs f-logo-box"></div>
  <div class="brand"><span class="sq"></span>Dash Meals</div>
  <span class="social" style="left:133px"><svg width="10" height="10"><circle cx="5" cy="5" r="2" fill="#333"/></svg></span>
  <span class="social" style="left:173px"><svg width="10" height="10"><circle cx="5" cy="5" r="2" fill="#333"/></svg></span>
  <span class="social" style="left:213px"><svg width="10" height="10"><circle cx="5" cy="5" r="2" fill="#333"/></svg></span>
  <span class="social" style="left:253px"><svg width="10" height="10"><circle cx="5" cy="5" r="2" fill="#333"/></svg></span>

  <div class="fcol" style="left:430px"><h6>COMPANY</h6><ul><li>Subscriptions</li><li>Business Plan</li><li>Gift Cards</li><li>Rewards</li><li>About Us</li><li>Contact Us</li></ul></div>
  <div class="fcol" style="left:576px"><h6>OTHERS LINK</h6><ul><li>My Account</li><li>Whishlist</li><li>My cart</li><li>Order Details</li><li>Payment Method</li></ul></div>
  <div class="fcol" style="left:738px"><h6>POLICY</h6><ul><li>Term Of Condition</li><li>Refund Policy</li><li>Shipping Policy</li><li>Privacy Policy</li></ul></div>
  <div class="fcol" style="left:884px"><h6>CONTACTS</h6>
    <div class="contact"><span class="ci"><svg width="10" height="12" viewBox="0 0 10 12"><path d="M5 11C1 6 1 5 1 4a4 4 0 0 1 8 0c0 1 0 2-4 7z" fill="none" stroke="var(--orange)" stroke-width="1.2"/></svg></span>Kingsford, ON, Canada K2P 4R8</div>
    <div class="contact"><span class="ci"><svg width="11" height="11" viewBox="0 0 11 11"><path d="M2 1l2 2-1 2c1 1 2 2 3 3l2-1 2 2-1 1C5 10 1 6 1 2z" fill="none" stroke="var(--orange)" stroke-width="1.1"/></svg></span>+1 555-014-2290</div>
    <div class="contact"><span class="ci"><svg width="12" height="9" viewBox="0 0 12 9"><rect x=".5" y=".5" width="11" height="8" fill="none" stroke="var(--orange)"/><path d="M.5.5l5.5 4 5.5-4" fill="none" stroke="var(--orange)"/></svg></span>hello@dashmeals.com</div>
  </div>

  <div class="abs f-rule"></div>
  <p class="abs copy">Copyright © 2022 <span>Dash</span>. All Rights Reserved.</p>
  <span class="card" style="left:537px;background:#e46c2b"></span>
  <span class="card" style="left:569px;background:#2b4a9b"></span>
  <span class="card" style="left:601px;background:#3a8fd6"></span>
  <span class="card" style="left:633px;background:#f0a04b"></span>
</footer>

</body>
</html>
```